Vel Framewright - Worpress Design

We are a consultancy to help builders to optimize their planning in order to save building costs. For that reason we need a website to offer our services, present our history, the mission and offer a plug-in for a first contact (including calendar), testimonials, a blog etc.
As an idea, I really like: https://www.kestrumadvisory.de/
Later on the website should be programmed in www.wolkanet.de in our Wordpress area. The text, of course, will be done by myself. The colors should be suitable to our recently designed logo.

```html
<!DOCTYPE html>
<html lang="en">
<head>
<meta charset="utf-8">
<title>Vel Framewright – Optimize &amp; Save Building Costs</title>
<link href="https://fonts.googleapis.com/css2?family=Nunito:wght@400;600;700;800;900&family=Nunito+Sans:wght@400;600;700&display=swap" rel="stylesheet">
<style>
:root{
  --gold:#d69e2a;
  --gold-light:#e8b446;
  --gold-dark:#b7851c;
  --ink:#1f1d1a;
  --text:#555;
  --muted:#8a8a8a;
  --soft:#f4f3f1;
  --dark:#2a2926;
  --darker:#1e1d1b;
  --olive:#3e3a30;
  --white:#fff;
}
*{box-sizing:border-box;margin:0;padding:0}
html,body{width:1200px;height:3438px;overflow:hidden}
body{position:relative;background:var(--white);font-family:"Nunito Sans",sans-serif;color:var(--text)}
.abs{position:absolute}
h1,h2,h3{font-family:"Nunito",sans-serif;color:var(--ink)}
.dash::after{content:"";display:inline-block;width:22px;height:4px;background:var(--gold);margin-left:12px;vertical-align:middle}
.dash-before::before{content:"";display:inline-block;width:22px;height:4px;background:var(--gold);margin-right:12px;vertical-align:middle}
.btn{position:absolute;display:flex;align-items:center;justify-content:center;gap:6px;height:29px;background:linear-gradient(90deg,var(--gold-light),var(--gold-dark));color:#fff;font-size:12px;border-radius:0 12px 0 12px;box-shadow:4px 6px 10px rgba(0,0,0,.18)}
.btn svg{width:11px;height:11px}

/* header */
.site-header{left:0;top:0;width:1200px;height:72px;background:rgba(255,255,255,.92);z-index:5}
.brand{left:232px;top:16px;display:flex;align-items:center;gap:10px;font-family:"Nunito",sans-serif;font-weight:800;font-size:20px;color:var(--gold)}
.brand-square{width:30px;height:30px;border:3px solid var(--gold)}
.topinfo{top:9px;font-size:9px;color:var(--gold);display:flex;align-items:center;gap:6px}
.topinfo i{width:11px;height:11px;border-radius:50%;background:var(--gold);display:inline-block}
.nav{top:42px;left:527px;display:flex;gap:28px;font-size:12px;color:#333;align-items:center}
.nav .active{color:var(--gold)}
.nav .contact{border:1px solid var(--gold);color:var(--gold);padding:5px 16px;border-radius:0 10px 0 10px}

/* hero */
.hero-photo{left:0;top:0;width:1200px;height:660px;background:linear-gradient(120deg,#d9dadc 0%,#c9cacb 40%,#b9b6b1 70%,#d7d6d3 100%)}
.hero-title{left:230px;top:240px;font-size:40px;font-weight:900;line-height:43px}
.hero-text{left:231px;top:334px;width:280px;font-size:11px;line-height:19px;color:#333}
.hero-wave{left:0;top:470px}
.scroll-hint{left:591px;top:591px}

/* about */
.about-photo{left:232px;top:714px;width:286px;height:389px;border-radius:0 60px 0 60px;background:linear-gradient(160deg,#a9c3dc 0%,#5a7fa3 45%,#1f3550 100%)}
.circle-soft{border-radius:50%;background:var(--soft)}
.about h2{left:569px;top:748px;font-size:38px;font-weight:900}
.about p{position:absolute;left:569px;width:315px;font-size:11px;line-height:19px;color:var(--muted)}

/* stats */
.stats-band{left:0;top:1120px}
.stat{top:1196px;width:180px;text-align:center;font-family:"Nunito",sans-serif}
.stat svg{width:36px;height:34px}
.stat b{display:block;font-size:19px;font-weight:800;color:var(--ink);margin-top:4px}
.stat span{font-family:"Nunito Sans",sans-serif;font-size:11px;color:#333}

/* services */
.services h2{left:232px;top:1381px;font-size:38px;font-weight:900}
.services .lead{left:232px;top:1437px;font-size:11px;line-height:19px;color:var(--muted);width:360px}
.service{position:absolute;width:287px;height:142px;border:1px solid var(--gold);border-radius:0 28px 0 28px;padding:14px 22px;background:#fff;color:var(--gold)}
.service svg.ico{width:34px;height:34px}
.service h3{color:var(--gold);font-size:13px;font-weight:800;margin:6px 0 8px}
.service p{font-size:10.5px;line-height:19px}
.service.active{background:var(--gold);color:#fff}
.service.active h3{color:#fff}
.service .go{position:absolute;right:16px;top:16px;width:28px;height:28px;border-radius:50%;background:#fff;display:flex;align-items:center;justify-content:center}

/* testimonials */
.testimonial-band{left:0;top:1950px}
.testimonials h2{left:0;width:1200px;text-align:center;top:2045px;font-size:38px;font-weight:900;color:#fff}
.quote{position:absolute;width:262px;height:141px;border:1px solid var(--gold);border-radius:0 30px 0 30px;padding:34px 20px 0 46px;font-style:italic;font-size:11px;line-height:19px;color:#fff}
.quote-mark{position:absolute;font-family:"Nunito",sans-serif;font-weight:900;font-size:90px;line-height:1;color:rgba(214,158,42,.35)}
.avatar{position:absolute;width:50px;height:50px;border-radius:50%;background:linear-gradient(160deg,#8c8a86,#3b3934);border:2px solid #fff}
.arrow{position:absolute;width:30px;height:30px;border-radius:50%;display:flex;align-items:center;justify-content:center}

/* insights */
.insights h2{right:232px;top:2517px;font-size:38px;font-weight:900}
.insights .lead{right:232px;top:2573px;font-size:11px;color:var(--muted)}
.post{position:absolute;top:2622px;width:230px}
.post .thumb{height:149px;border-radius:0 26px 0 26px;position:relative;overflow:hidden}
.post .tag{position:absolute;left:0;bottom:0;width:94px;height:22px;background:var(--gold);color:#fff;font-size:11px;padding:4px 12px;border-radius:0 12px 0 0}
.post h3{font-size:11px;font-weight:800;margin:14px 0 6px}
.post p{font-size:10.5px;line-height:15px;color:var(--muted)}
.post .more{display:block;margin-top:10px;color:var(--gold);font-weight:700;font-size:11px;font-family:"Nunito",sans-serif}

/* footer */
.footer-wave{left:0;top:2990px}
.footer{left:0;top:3110px;width:1200px;height:328px;background:var(--dark)}
.footer .brand{top:3190px}
.foot-info{left:232px;font-size:11px;color:var(--gold);display:flex;align-items:center;gap:12px}
.foot-info i{width:12px;height:12px;border-radius:50%;background:var(--gold);display:inline-block}
.foot-col{top:3185px;font-size:11px;color:var(--gold)}
.foot-col h4{color:#eee;font-weight:600;font-size:13px;margin-bottom:12px;font-family:"Nunito",sans-serif}
.foot-col li{list-style:none;margin-bottom:11px}
.social{top:3222px;left:818px;display:flex;gap:10px}
.social i{width:28px;height:28px;border-radius:50%;background:var(--gold);display:block}
.bottom-bar{left:0;top:3400px;width:1200px;height:38px;background:var(--darker);font-size:10px;color:#888;display:flex;justify-content:space-between;align-items:center;padding:0 232px 0 230px}
</style>
</head>
<body>

<!-- HERO -->
<div class="abs hero-photo" role="img" aria-label="Photo of three consultants leaning over building plans on a desk"></div>
<div class="abs" style="left:150px;top:150px;width:420px;height:300px;border-radius:50%;background:rgba(255,255,255,.35)"></div>
<svg class="abs hero-wave" width="1200" height="190" viewBox="0 0 1200 190">
  <path d="M0 80 C150 40 230 190 420 185 C600 180 760 70 920 20 C1020 -5 1120 50 1200 40 V190 H0Z" fill="#f6f1e6"/>
  <path d="M0 95 C160 70 260 150 420 170 C560 185 700 100 860 55 C990 20 1100 60 1200 70 V190 H0Z" fill="#fff"/>
</svg>
<svg class="abs scroll-hint" width="18" height="24" viewBox="0 0 18 24"><rect x="1" y="1" width="16" height="22" rx="8" fill="none" stroke="#b7851c" stroke-width="1.5"/><path d="M9 6v9M5 12l4 4 4-4" stroke="#b7851c" stroke-width="1.5" fill="none"/></svg>

<header class="abs site-header">
  <div class="abs brand"><span class="brand-square"></span>Vel Framewright</div>
  <div class="abs topinfo" style="left:717px"><i></i>support@wolkanet.de</div>
  <div class="abs topinfo" style="left:838px"><i></i>14B Ufergasse, Berlin, Germany</div>
  <nav class="abs nav">
    <span class="active">Home</span><span>About Us</span><span>Services</span><span>Testimonials</span><span>Blog</span><span class="contact">Contact Us</span>
  </nav>
</header>

<h1 class="abs hero-title">Optimize &amp; Save<br>Building Costs</h1>
<p class="abs hero-text">Lorem ipsum dolor sit amet, consectetur adipiscing elit, sed do eiusmod tempor incididunt ut labore us commodo viverra maecenas facilisis.</p>
<a class="btn" style="left:231px;top:405px;width:143px">Free Consultation <svg viewBox="0 0 12 12"><path d="M1 6h9M6 2l4 4-4 4" stroke="#fff" stroke-width="1.6" fill="none"/></svg></a>

<!-- ABOUT -->
<section class="about">
  <div class="abs about-photo" role="img" aria-label="Photo looking up at glass office towers against a blue sky"></div>
  <div class="abs circle-soft" style="left:752px;top:715px;width:160px;height:160px"></div>
  <h2 class="abs dash">Who We Are</h2>
  <p style="top:808px">Lorem ipsum dolor sit amet, consectetur adipiscing elit, sed do eiusmod tempor incididunt ut labore et dolore magna aliqua. Quis ipsum suspendisse facilisis.</p>
  <p style="top:878px">Dolore magna aliqua. Quis ipsum suspendisse ultrices gravida. Risus commodo viverra maecenas accumsan lacus vel facilisis.</p>
  <a class="btn" style="left:569px;top:989px;width:125px">Our History <svg viewBox="0 0 12 12"><path d="M1 6h9M6 2l4 4-4 4" stroke="#fff" stroke-width="1.6" fill="none"/></svg></a>
</section>

<!-- STATS -->
<svg class="abs stats-band" width="1200" height="260" viewBox="0 0 1200 260">
  <path d="M0 90 C80 20 200 20 330 40 C470 60 560 60 700 40 C860 10 1000 0 1200 30 V230 C1050 200 950 250 800 245 C650 240 560 210 420 215 C260 220 100 250 0 250Z" fill="#f7f6f5"/>
</svg>
<div class="abs stat" style="left:190px"><svg viewBox="0 0 36 34" fill="none" stroke="#d69e2a" stroke-width="1.3"><circle cx="18" cy="7" r="4"/><circle cx="9" cy="15" r="3.5"/><circle cx="27" cy="15" r="3.5"/><path d="M3 30c0-6 4-9 6-9s6 3 6 9M21 30c0-6 4-9 6-9s6 3 6 9M11 22c2-4 5-6 7-6s5 2 7 6"/></svg><b>563</b><span>Satisfied Clients</span></div>
<div class="abs stat" style="left:393px;top:1194px"><svg viewBox="0 0 36 34" fill="none" stroke="#d69e2a" stroke-width="1.3"><rect x="3" y="12" width="12" height="20"/><rect x="15" y="4" width="10" height="28"/><rect x="25" y="14" width="8" height="18"/><path d="M6 16h6M6 21h6M6 26h6M18 9h4M18 14h4M18 19h4M18 24h4M27 19h4M27 24h4"/></svg><b>1257</b><span>Successful Projects</span></div>
<div class="abs stat" style="left:616px"><svg viewBox="0 0 36 34" fill="none" stroke="#d69e2a" stroke-width="1.5"><path d="M3 10c0-4 3-6 6-6s6 2 6 6c0 5-12 12-12 20h12"/><rect x="20" y="4" width="13" height="26" rx="6"/></svg><b>20</b><span>Years of Experience</span></div>
<div class="abs stat" style="left:828px"><svg viewBox="0 0 36 34" fill="none" stroke="#d69e2a" stroke-width="1.3"><circle cx="10" cy="12" r="4"/><circle cx="26" cy="12" r="4"/><path d="M5 9h10M21 9h10M2 32v-8c0-4 4-6 8-6s8 2 8 6v8M18 32v-8c0-4 4-6 8-6s8 2 8 6v8"/></svg><b>42</b><span>Team Members</span></div>

<!-- SERVICES -->
<section class="services">
  <div class="abs circle-soft" style="left:158px;top:1350px;width:165px;height:165px"></div>
  <div class="abs circle-soft" style="left:780px;top:1610px;width:325px;height:325px"></div>
  <h2 class="abs dash">Our Services</h2>
  <p class="abs lead">Dolore magna aliqua. Quis ipsum suspendisse ultrices gravida. Risus commodo viverra maecenas accumsan lacus vel facilisis.</p>

  <div class="service active" style="left:375px;top:1521px">
    <svg class="ico" viewBox="0 0 34 34" fill="none" stroke="#fff" stroke-width="1.3"><circle cx="12" cy="10" r="5"/><path d="M6 8h12M2 32v-7c0-5 5-8 10-8s10 3 10 8v7"/><rect x="20" y="20" width="12" height="12"/></svg>
    <span class="go"><svg width="12" height="12" viewBox="0 0 12 12"><path d="M4 2l4 4-4 4" stroke="#d69e2a" stroke-width="1.8" fill="none"/></svg></span>
    <h3>Planning Consultation</h3>
    <p>Dolore magna aliqua. Quis ipsum sus pendisse ul trices gravida. Risus commodo viverra mac decenas accumsan lacus vel facilisis.</p>
  </div>
  <svg class="abs" style="left:636px;top:1641px" width="20" height="28" viewBox="0 0 20 28"><path d="M1 1v22l6-6 4 9 3-1-4-9h8z" fill="#111" stroke="#fff" stroke-width="1"/></svg>

  <div class="service" style="left:682px;top:1521px">
    <svg class="ico" viewBox="0 0 34 34" fill="none" stroke="#d69e2a" stroke-width="1.3"><circle cx="17" cy="17" r="6"/><circle cx="17" cy="17" r="2.5"/><path d="M4 17a13 13 0 0 1 22-9M30 17a13 13 0 0 1-22 9M26 3v5h-5M8 31v-5h5"/></svg>
    <h3>Logistics Optimization</h3>
    <p>Ipsum sus pendisse ul trices gravida. Risus commodo viverra mac decenas accumsan lacus vel facilisis.</p>
  </div>

  <div class="service" style="left:232px;top:1687px">
    <svg class="ico" viewBox="0 0 34 34" fill="none" stroke="#d69e2a" stroke-width="1.3"><rect x="3" y="3" width="28" height="28"/><path d="M3 10h28M10 3v28M14 14h13v13H14z"/></svg>
    <h3>Planning Optimization</h3>
    <p>Pendisse ul trices gravida. Risus commodo viverra mac decenas accumsan lacus vel facilisis ultra deloe ipsum lorem.</p>
  </div>

  <div class="service" style="left:539px;top:1687px">
    <svg class="ico" viewBox="0 0 34 34" fill="none" stroke="#d69e2a" stroke-width="1.3"><path d="M3 30h28M6 30V14l6-5 6 5v16M20 30V18h10v12M10 19h4M10 24h4"/><circle cx="26" cy="8" r="4"/></svg>
    <h3>Smart Construction Optimization</h3>
    <p>Quis ipsum sus pendisse ul trices gravida. Risus commodo viverra mac decenas accumsan lacus vel facilisis magna aliqua.</p>
  </div>

  <a class="btn" style="left:529px;top:1873px;width:141px">Get Started <svg viewBox="0 0 12 12"><path d="M1 6h9M6 2l4 4-4 4" stroke="#fff" stroke-width="1.6" fill="none"/></svg></a>
</section>

<!-- TESTIMONIALS -->
<svg class="abs testimonial-band" width="1200" height="490" viewBox="0 0 1200 490">
  <defs><linearGradient id="tg" x1="0" y1="0" x2="1" y2="1"><stop offset="0" stop-color="#4a463b"/><stop offset="1" stop-color="#34312a"/></linearGradient></defs>
  <path d="M0 70 C120 90 300 20 460 12 C620 5 700 110 860 120 C1000 130 1120 60 1200 30 V420 C1120 400 1000 350 880 380 C720 420 620 470 440 475 C260 480 120 370 0 390Z" fill="#ededec"/>
  <path d="M0 95 C160 100 300 20 460 20 C620 22 720 120 880 130 C1010 138 1120 80 1200 50 V380 C1100 360 1000 420 860 440 C700 462 600 480 420 470 C260 460 120 400 0 410Z" fill="url(#tg)"/>
</svg>
<div class="abs" role="img" aria-label="Faint photo of an office desk with laptop and plans" style="left:0;top:2000px;width:1200px;height:380px;background:radial-gradient(ellipse at 30% 40%,rgba(255,255,255,.07),transparent 60%)"></div>
<section class="testimonials">
  <h2 class="abs dash">Testimonials</h2>
  <span class="quote-mark" style="left:290px;top:2100px">“</span>
  <div class="quote" style="left:304px;top:2152px">Pendisse ul trices gravida. Risus commodo viverra mac decenas accumsan lacus vel facilisis ultra deloe ipsum lorem.</div>
  <div class="avatar" role="img" aria-label="Client portrait" style="left:280px;top:2196px"></div>
  <span class="quote-mark" style="left:642px;top:2100px">“</span>
  <div class="quote" style="left:657px;top:2152px">Ultrices gravida. Risus com lem odo viverra mac decenas accum san lacus vel facilisis ultra deloe ipsum lorem dolores.</div>
  <div class="avatar" role="img" aria-label="Client portrait" style="left:631px;top:2196px"></div>
  <span class="arrow" style="left:232px;top:2206px;border:1.5px solid var(--gold)"><svg width="12" height="12" viewBox="0 0 12 12"><path d="M8 2L4 6l4 4" stroke="#d69e2a" stroke-width="1.8" fill="none"/></svg></span>
  <span class="arrow" style="left:938px;top:2206px;background:var(--gold)"><svg width="12" height="12" viewBox="0 0 12 12"><path d="M4 2l4 4-4 4" stroke="#2a2926" stroke-width="1.8" fill="none"/></svg></span>
</section>

<!-- INSIGHTS -->
<section class="insights">
  <div class="abs circle-soft" style="left:95px;top:2595px;width:330px;height:330px"></div>
  <div class="abs circle-soft" style="left:868px;top:2918px;width:180px;height:180px"></div>
  <h2 class="abs dash-before">Latest Insights</h2>
  <p class="abs lead">Read our latest insights directly from our blog</p>

  <article class="post" style="left:232px">
    <div class="thumb" role="img" aria-label="Photo of a blue glass skyscraper" style="background:linear-gradient(160deg,#e7eef6,#7e9dc4 50%,#2c4670)"><span class="tag">Planning</span></div>
    <h3>Construction Planning Checklist</h3>
    <p>Consectetur adipiscing elit, sed do eiusmod tempor incididunt ut labore et dolore mag dna aliqua. Quis ipsum suspendisse ultrices gravida. Risus commodo...</p>
    <span class="more">Read More →</span>
  </article>
  <article class="post" style="left:485px">
    <div class="thumb" role="img" aria-label="Black and white photo of a building under construction with cranes" style="background:linear-gradient(180deg,#efefef,#bdbdbd 60%,#6f6f6f)"><span class="tag">Construction</span></div>
    <h3>Optimization in Equipment Distribution</h3>
    <p>Sed do eiusmod tempor incididunt ut labore et dolore magna aliqua. Quis ipsum sus pendisse ultrices gravida. Cenas accumsan lacus vel facilisis...</p>
    <span class="more">Read More →</span>
  </article>
  <article class="post" style="left:738px">
    <div class="thumb" role="img" aria-label="Photo of hands working on a tablet over architectural drawings" style="background:linear-gradient(150deg,#d8d3cb,#f1efea 50%,#9cc7d8)"><span class="tag">Logistics</span></div>
    <h3>Planning Ahead</h3>
    <p>Sit dolore tetur adipiscing elit, sed do eiusmod tempor incididunt ut labore et dolore magna aliqua. commodo viverra maecenas accumsan lacusis...</p>
    <span class="more">Read More →</span>
  </article>

  <a class="btn" style="left:529px;top:2937px;width:141px">Visit Blog <svg viewBox="0 0 12 12"><path d="M1 6h9M6 2l4 4-4 4" stroke="#fff" stroke-width="1.6" fill="none"/></svg></a>
</section>

<!-- FOOTER -->
<svg class="abs footer-wave" width="1200" height="125" viewBox="0 0 1200 125">
  <path d="M0 95 C120 60 240 50 360 40 C460 32 560 70 700 50 C850 28 980 0 1100 15 C1150 22 1180 30 1200 35 V125 H0Z" fill="#6a5327"/>
  <path d="M0 105 C100 115 200 75 330 60 C470 45 560 80 700 70 C860 58 980 20 1200 55 V125 H0Z" fill="#2a2926"/>
</svg>
<footer class="abs footer"></footer>
<div class="abs brand" style="top:3190px;color:var(--gold)"><span class="brand-square"></span>Vel Framewright</div>
<div class="abs foot-info" style="top:3243px"><i></i>14B Ufergasse, Berlin, Germany</div>
<div class="abs foot-info" style="top:3267px"><i></i>support@wolkanet.de</div>
<div class="abs foot-info" style="top:3290px"><i></i>310 5521 0847</div>
<div class="abs foot-col" style="left:520px"><h4>Quick Links</h4><ul><li>About Us</li><li>Services</li><li>Testimonials</li><li>Blog</li><li>Contact Us</li></ul></div>
<div class="abs foot-col" style="left:663px"><h4>Useful Links</h4><ul><li>Privacy Policy</li><li>Terms &amp; Conditions</li><li>Support</li><li>FAQ</li></ul></div>
<div class="abs foot-col" style="left:818px"><h4>Social Media</h4></div>
<div class="abs social" aria-label="Social media links"><i></i><i></i><i></i></div>
<div class="abs bottom-bar"><span>www.wolkanet.de</span><span>All Rights Reserved 2023 Vel Framewright</span></div>

</body>
</html>
```